Slide desk development crimson ledge holdings

I am looking to expand the range of slide templates we have using our new branded powerpoint deck so the team have more options.

Target Market(s)

We operate in the construction sector

Industry/Entity Type

Construction

Requirements
Must have
• Picture linking back to construction

```html
<!DOCTYPE html>
<html lang="en">
<head>
<meta charset="utf-8">
<title>Crimson Ledge Holdings — Presentation Template</title>
<link href="https://fonts.googleapis.com/css2?family=Poppins:ital,wght@0,300;0,400;0,500;0,600;0,700;1,400&display=swap" rel="stylesheet">
<style>
:root{
  --black:#000;
  --white:#fff;
  --green:#95e06c;
  --gap:#cfcfcf;
  --muted:#d9d9d9;
  --rule:#2a3350;
  --photo-site-a:#8a8f86;
  --photo-site-b:#d9dcd6;
  --photo-sky-a:#1e5fb0;
  --photo-sky-b:#c9a24a;
  --photo-warm-a:#b59a74;
  --photo-warm-b:#e8e2d8;
  --photo-portrait-a:#4a6f86;
  --photo-portrait-b:#e07a2c;
}
*{margin:0;padding:0;box-sizing:border-box}
html,body{width:1200px;height:4792px;overflow:hidden}
body{background:var(--gap);font-family:'Poppins',sans-serif;color:var(--white);position:relative}
.slide{position:absolute;left:0;width:1200px;overflow:hidden;background:var(--black)}
.abs{position:absolute}
.photo{position:absolute}
p{font-weight:300}

/* title */
.s-title{top:0;height:673px}
.brand{left:0;width:1200px;top:262px;display:flex;justify-content:center;align-items:center;gap:22px}
.brand-dot{width:56px;height:56px;border-radius:50%;background:var(--green)}
.brand-name{font-size:54px;font-weight:500;color:var(--white)}
.title-sub{left:0;width:1200px;top:550px;text-align:center;font-size:22px;letter-spacing:5px;font-weight:400}

/* intro */
.s-intro{top:682px;height:678px}
.s-intro .photo{left:0;top:0;width:1200px;height:368px;background:linear-gradient(170deg,var(--photo-site-a),var(--photo-site-b) 60%,#eef0ec)}
.intro-h{left:0;width:1200px;top:408px;text-align:center;color:var(--green);font-size:36px;font-weight:600}
.intro-p{left:175px;width:850px;top:486px;text-align:center;font-size:13.5px;line-height:27px}

/* key personnel */
.s-people{top:1369px;height:677px;background:var(--white);color:var(--black)}
.people-h{left:149px;top:136px;font-size:40px;font-weight:600}
.people-h span{color:var(--green)}
.person-name{left:149px;top:204px;font-size:20px;font-weight:600}
.person-role{left:149px;top:230px;font-size:17px;font-style:italic;font-weight:300}
.people-box{left:140px;top:274px;width:823px;height:284px;background:var(--black);color:var(--white);padding:24px 44px;font-size:14px;line-height:21.5px}
.portrait{left:851px;top:136px;width:224px;height:224px;border-radius:50%;border:3px solid #222;background:radial-gradient(circle at 50% 40%,#c9b8a6,#6e7a86 70%,#2b2f36)}

/* what we do */
.s-what{top:2055px;height:680px}
.s-what .photo{left:0;top:91px;width:443px;height:587px;background:linear-gradient(160deg,var(--photo-portrait-a),#b9c2c6 45%,var(--photo-portrait-b))}
.what-h{left:511px;top:96px;font-size:54px;font-weight:700}
.item{position:absolute;left:511px;width:620px}
.item-icon{position:absolute;left:0;top:8px;width:66px;height:66px}
.item-title{position:absolute;left:97px;top:0;font-size:21px;font-weight:600}
.item-text{position:absolute;left:88px;top:32px;width:520px;font-size:14px;line-height:26px}

/* who we are */
.s-who{top:2744px;height:675px}
.who-crane{left:0;top:56px;width:288px;height:564px;background:linear-gradient(200deg,var(--photo-sky-a),#4d86c4 50%,var(--photo-sky-b))}
.who-team{left:307px;top:89px;width:299px;height:497px;background:linear-gradient(180deg,var(--photo-warm-a),var(--photo-warm-b) 55%,#5a5a5a)}
.who-h{left:670px;top:136px;font-size:38px;font-weight:400;line-height:49px}
.who-p{left:670px;top:244px;width:410px;font-size:14px;line-height:27px}
.who-sub{left:676px;top:384px;font-size:16px;font-weight:500}
.who-badge{left:665px;top:426px;width:80px;height:80px;border-radius:50%;background:var(--green);display:flex;align-items:center;justify-content:center}
.who-note{left:766px;top:430px;width:320px;font-size:14px;line-height:27px}

/* services */
.s-services{top:3428px;height:673px}
.svc-accent{left:0;top:0}
.svc-bar{left:0;top:124px;width:121px;height:9px;background:var(--green)}
.svc-h{left:154px;top:112px;font-size:32px;font-weight:600;line-height:40px}
.svc-p{left:154px;top:210px;width:430px;font-size:13.5px;line-height:21.6px}
.stat{position:absolute;left:641px}
.stat svg{position:absolute;left:0;top:0}
.stat-val{position:absolute;left:127px;top:-12px;font-size:28px;font-weight:600}
.stat-label{position:absolute;left:127px;top:30px;font-size:13px;letter-spacing:4px;width:170px;line-height:18px}

/* timeline */
.s-timeline{top:4114px;height:678px}
.s-timeline .photo{left:0;top:0;width:450px;height:678px;background:linear-gradient(200deg,var(--photo-sky-a),#3f7fc6 45%,var(--photo-sky-b))}
.tl-h{left:523px;top:48px;font-size:56px;font-weight:700}
.tl-table{position:absolute;left:513px;top:142px;width:562px;border-collapse:collapse;font-size:18px}
.tl-table td,.tl-table th{border:2px solid var(--rule);padding:0 14px;text-align:left;font-weight:400;line-height:24px;vertical-align:middle}
.tl-table th{font-weight:500}
.tl-table .c1{width:337px}
</style>
</head>
<body>

<section class="slide s-title">
  <div class="abs brand"><span class="brand-dot"></span><span class="brand-name">Crimson Ledge Holdings</span></div>
  <div class="abs title-sub">PRESENTATION TEMPLATE</div>
</section>

<section class="slide s-intro">
  <div class="photo" role="img" aria-label="Aerial photo of construction workers in hi-vis vests on a concrete slab with rebar"></div>
  <h2 class="abs intro-h">INTRODUCTION</h2>
  <p class="abs intro-p">Lorem ipsum dolor sit amet, consectetur adipiscing elit, sed do eiusmod tempor incididunt ut labore et dolore magna aliqua. Ut enim ad minim veniam, quis nostrud exercitation ullamco laboris nisi ut aliquip ex ea commodo consequat. Duis aute irure dolor in reprehenderit in voluptate velit esse cillum dolore eu fugiat nulla pariatur.</p>
</section>

<section class="slide s-people">
  <h2 class="abs people-h">Key <span>Personnel</span></h2>
  <div class="abs person-name">Daniel Harcourt</div>
  <div class="abs person-role">CEO (joined 2020)</div>
  <div class="abs people-box"><p>Lorem ipsum dolor sit amet, consectetuer adipiscing elit, sed diam nonummy nibh euismod tincidunt ut laoreet dolore magna aliquam erat volutpat. Ut wisi enim ad minim veniam, quis nostrud exerci tation ullamcorper suscipit lobortis nisl ut aliquip ex ea commodo consequat. Duis autem vel eum iriure dolor in hendrerit in vulputate velit esse molestie consequat, vel illum dolore eu feugiat nulla facilisis at vero eros et accumsan et iusto odio dignissim qui blandit praesent luptatum zzril delenit augue duis dolore te feugait nulla facilisi.<br>Lorem ipsum dolor sit amet, cons ectetuer adipiscing elit, sed diam nonummy nibh euismod tincidunt ut laoreet dolore magna aliquam erat volutpat. Ut wisi enim ad minim veniam, quis nostrud exerci tation ullamcorper.</p></div>
  <div class="abs portrait" role="img" aria-label="Circular portrait photo of the CEO"></div>
</section>

<section class="slide s-what">
  <div class="photo" role="img" aria-label="Photo of a smiling construction worker in a white hard hat and orange hi-vis vest"></div>
  <h2 class="abs what-h">What&nbsp; We Do</h2>
  <div class="item" style="top:232px">
    <svg class="item-icon" viewBox="0 0 66 66"><circle cx="33" cy="33" r="30" fill="#fff"/><path d="M20 24h26a3 3 0 0 1 3 3v12a3 3 0 0 1-3 3H30l-7 6v-6h-3a3 3 0 0 1-3-3V27a3 3 0 0 1 3-3z" fill="none" stroke="#000" stroke-width="2.5"/><circle cx="26" cy="33" r="2" fill="#000"/><circle cx="33" cy="33" r="2" fill="#000"/><circle cx="40" cy="33" r="2" fill="#000"/></svg>
    <div class="item-title">First Content</div>
    <p class="item-text">Leverage agile frameworks to provide a robust synopsis for high level overviews. Iterative approaches to corporate strategy foster collaborative thinking to further the overall value proposition.</p>
  </div>
  <div class="item" style="top:366px">
    <svg class="item-icon" viewBox="0 0 66 66"><circle cx="33" cy="33" r="30" fill="#fff"/><circle cx="33" cy="35" r="13" fill="none" stroke="#000" stroke-width="2.5"/><circle cx="33" cy="35" r="8" fill="none" stroke="#000" stroke-width="2"/><path d="M22 22l-3-3M44 22l3-3" stroke="#000" stroke-width="2.5"/></svg>
    <div class="item-title">Second Content</div>
    <p class="item-text">Leverage agile frameworks to provide a robust synopsis for high level overviews. Iterative approaches to corporate strategy foster collaborative thinking to further the overall value proposition.</p>
  </div>
  <div class="item" style="top:497px">
    <svg class="item-icon" viewBox="0 0 66 66"><circle cx="33" cy="33" r="30" fill="#fff"/><rect x="22" y="24" width="22" height="18" fill="none" stroke="#000" stroke-width="2.5"/><path d="M33 18v6M26 42l-4 8M40 42l4 8M18 42h30" stroke="#000" stroke-width="2.5"/></svg>
    <div class="item-title">Third Content</div>
    <p class="item-text">Leverage agile frameworks to provide a robust synopsis for high level overviews. Iterative approaches to corporate strategy foster collaborative thinking to further the overall value proposition</p>
  </div>
</section>

<section class="slide s-who">
  <div class="photo who-crane" role="img" aria-label="Photo of a tower crane beside a high-rise under construction against blue sky"></div>
  <div class="photo who-team" role="img" aria-label="Photo of two engineers in hard hats reviewing plans on site"></div>
  <h2 class="abs who-h">Who<br>We Are?</h2>
  <p class="abs who-p">Lorem ipsum dolor sit amet, consectetur adipiscing elit, sed do eiusmod tempor incididunt ut labore et dolore magna aliqua. Ut enim ad minim veniam, quis nostrud exercitation</p>
  <div class="abs who-sub">Subtitle Here</div>
  <div class="abs who-badge"><svg width="40" height="32" viewBox="0 0 40 32"><path d="M4 6h18v14H4zM22 10h8l6 6v4H22z" fill="#000"/><circle cx="10" cy="24" r="4" fill="#000"/><circle cx="30" cy="24" r="4" fill="#000"/></svg></div>
  <p class="abs who-note">Lorem ipsum dolor sit amet, consectetur adipiscing elit, sed do eiusmod tempor incididunt ut labore et dolore magna aliqua. Ut enim ad minim.</p>
</section>

<section class="slide s-services">
  <svg class="abs svc-accent" width="1200" height="673"><polygon points="1140,0 1200,0 1200,673 1017,673" fill="var(--green)"/></svg>
  <div class="abs svc-bar"></div>
  <h2 class="abs svc-h">Our Special<br>Services</h2>
  <p class="abs svc-p">Lorem ipsum dolor sit amet, consectetuer adipiscing elit, sed diam nonummy nibh euismod tincidunt ut laoreet dolore magna aliquam erat volutpat. Ut wisi enim ad minim veniam, quis nostrud exerci tation ullamcorper suscipit lobortis nisl ut aliquip ex ea commodo consequat. Duis autem vel eum iriure dolor in hendrerit in vulputate velit esse molestie consequat, vel illum dolore eu feugiat nulla facilisis at vero eros et accumsan et iusto odio dignissim qui blandit praesent luptatum zzril delenit augue duis dolore te feugait nulla facilisi.<br>Lorem ipsum dolor sit amet, cons ectetuer adipiscing elit, sed diam nonummy nibh euismod tincidunt ut laoreet dolore magna aliquam erat volutpat. Ut wisi enim ad minim veniam, quis nostrud exerci tation ullamcorper suscipit lobortis nisl ut aliquip ex ea commodo consequat.</p>
  <div class="stat" style="top:215px">
    <svg width="88" height="60" viewBox="0 0 88 60" fill="none" stroke="#fff" stroke-width="2.5"><rect x="4" y="22" width="46" height="22"/><path d="M50 28h18l10 10v6H50z"/><ellipse cx="24" cy="18" rx="18" ry="10"/><circle cx="16" cy="48" r="6"/><circle cx="64" cy="48" r="6"/></svg>
    <div class="stat-val">40%</div><div class="stat-label">CONSTRUCTION</div>
  </div>
  <div class="stat" style="top:343px">
    <svg width="88" height="64" viewBox="0 0 88 64" fill="none" stroke="#fff" stroke-width="2.5"><path d="M8 30L40 6l32 24"/><path d="M14 26v34h52V26"/><path d="M22 60V46M32 60V40M42 60V34M52 60V42"/><path d="M20 40l12-10 10 6 18-16"/></svg>
    <div class="stat-val">40%</div><div class="stat-label">ARCHITECTURE</div>
  </div>
  <div class="stat" style="top:484px">
    <svg width="88" height="80" viewBox="0 0 88 80" fill="none" stroke="#fff" stroke-width="2.5"><path d="M16 60V20l44 24"/><path d="M30 30l10-6M44 38l10-6"/><rect x="52" y="46" width="26" height="18"/><circle cx="16" cy="70" r="8" fill="#fff"/></svg>
    <div class="stat-val">20%</div><div class="stat-label">Service 3</div>
  </div>
</section>

<section class="slide s-timeline">
  <div class="photo" role="img" aria-label="Photo of a tower crane and high-rise building under construction"></div>
  <h2 class="abs tl-h">Timeline</h2>
  <table class="tl-table">
    <tr style="height:52px"><th class="c1">Phase</th><th>Week</th></tr>
    <tr style="height:52px"><td>Kickoff Meeting</td><td>1</td></tr>
    <tr style="height:101px"><td>Analytics Implementations, Website Audit, Content and Keyword Research</td><td>1–2</td></tr>
    <tr style="height:52px"><td>Digital Strategy Development</td><td>2–3</td></tr>
    <tr style="height:50px"><td>Present Strategy</td><td>4</td></tr>
    <tr style="height:50px"><td>Content Development</td><td>4–8</td></tr>
    <tr style="height:75px"><td>Paid Media and Email Campaign Setup</td><td>6–7</td></tr>
    <tr style="height:49px"><td>Go Live</td><td>8</td></tr>
  </table>
</section>

</body>
</html>
```